Korvane Plumbing Business cards

Company is Korvane Plumbing.
name Dorian Malvessey, I am a plumber, drainer, gasfitter and roofer
Mobile: 0461 590 314
Email address: info@korvaneplumbing.example (check out my website for some ideas)
Website: www.korvaneplumbing.example
ABN: 42 198 603 771
LIC: 516042D

I am reliable all round plumber. I am a 24 hour emergency service. Korvane Plumbing is a professional plumbing service in the Illawarra, South Coast, Southern Sydney and Southern Highland regions of NSW. We offer a 24 hour emergency service for piece of mind to our customers. Call us now to see how we can help you. Korvane Plumbing approaches every job with attention to detail and excellent customer service. With our superior workmanship you can be confident that the job will be done right the first time around. You can rest assured with results that are guaranteed to last.

Target Market(s)

the general public

Contact Information for Business Card

look up website for some ideas something with similar colours to logo and new modern and to catch the eye.

Colors
fdfdfd
ffffff
000000
7f7f7f
aaaaaa
33a6d7
0492cd

Requirements
Must have
• all contact details
• company- Korvane Plumbing
• name- Dorian Malvessey
• number mobile- 0461 590 314
• Email address- info@korvaneplumbing.example
• Website- www.korvaneplumbing.example
• ABN- 42 198 603 771
• LIC- 516042D

```html
<!DOCTYPE html>
<html lang="en">
<head>
<meta charset="utf-8">
<title>Korvane Plumbing – Business Cards</title>
<link rel="stylesheet" href="https://fonts.googleapis.com/css2?family=Montserrat:wght@400;500;600;700&display=swap">
<style>
  :root {
    --card-black: #0b0b0c;
    --white: #ffffff;
    --grey-dark: #7f7f7f;
    --grey-light: #aaaaaa;
    --blue: #33a6d7;
    --blue-deep: #0492cd;
    --backdrop: #e6e6e6;
  }
  * { box-sizing: border-box; margin: 0; padding: 0; }
  html, body {
    width: 1200px; height: 831px; overflow: hidden;
    background: var(--backdrop);
    font-family: "Montserrat", sans-serif;
  }
  .sheet {
    position: relative; width: 1200px; height: 831px;
    display: flex; align-items: center; justify-content: center; gap: 40px;
  }
  .card {
    position: relative; width: 540px; height: 310px;
    background: var(--card-black); overflow: hidden;
    box-shadow: 0 10px 28px rgba(0,0,0,0.25);
  }

  /* Back of card */
  .card-back { display: flex; align-items: center; justify-content: center; }
  .back-brand {
    color: var(--grey-light); font-weight: 700; font-size: 30px;
    letter-spacing: 1px; line-height: 1; white-space: nowrap;
  }

  /* Front of card */
  .brand {
    position: absolute; right: 30px; top: 52px;
    color: var(--blue); font-weight: 700; font-size: 32px;
    letter-spacing: 0.5px; line-height: 1; white-space: nowrap;
  }
  .holder {
    position: absolute; right: 30px; top: 104px;
    font-size: 22px; letter-spacing: 0.5px; line-height: 1; white-space: nowrap;
  }
  .holder .first { color: var(--grey-light); font-weight: 400; }
  .holder .last { color: var(--blue); font-weight: 600; }

  .contacts {
    position: absolute; left: 222px; top: 142px; list-style: none;
  }
  .contacts li {
    display: flex; align-items: center; gap: 9px;
    color: var(--white); font-size: 14px; font-weight: 500;
    height: 23px; white-space: nowrap;
  }
  .contact-icon {
    width: 14px; height: 14px; border-radius: 50%;
    background: var(--blue); display: flex; align-items: center; justify-content: center;
    flex: none;
  }

  .credentials-band {
    position: absolute; left: 0; top: 0; width: 540px; height: 310px;
    background: var(--blue);
    clip-path: polygon(0 222px, 130px 244px, 540px 262px, 540px 310px, 0 310px);
  }
  .credentials-text {
    position: absolute; left: 200px; top: 276px;
    color: var(--white); font-size: 15px; font-weight: 500; letter-spacing: 0.5px;
    white-space: nowrap;
  }
  .tool-art {
    position: absolute; left: 30px; top: 140px; width: 112px; height: 116px;
    background: linear-gradient(135deg, #9a9a9a, #6f6f6f);
  }
</style>
</head>
<body>
  <main class="sheet">
    <section class="card card-back" aria-label="Business card back">
      <p class="back-brand">KORVANE PLUMBING</p>
    </section>

    <section class="card card-front" aria-label="Business card front">
      <div class="credentials-band"></div>
      <p class="brand">KORVANE PLUMBING</p>
      <p class="holder"><span class="first">DORIAN</span> <span class="last">MALVESSEY</span></p>

      <ul class="contacts">
        <li>
          <span class="contact-icon">
            <svg width="8" height="8" viewBox="0 0 10 10"><path d="M2 1 L4 1 L4.6 3 L3.5 4 Q4.5 6 6 6.5 L7 5.4 L9 6 L9 8 Q8.5 9 7.5 9 Q1 8.5 1 2 Q1 1 2 1Z" fill="#ffffff"/></svg>
          </span>
          0461 590 314
        </li>
        <li>
          <span class="contact-icon">
            <svg width="8" height="8" viewBox="0 0 10 10"><rect x="1" y="2.5" width="8" height="5.5" fill="#ffffff"/><path d="M1 2.5 L5 5.5 L9 2.5" stroke="#33a6d7" stroke-width="0.9" fill="none"/></svg>
          </span>
          info@korvaneplumbing.example
        </li>
        <li>
          <span class="contact-icon">
            <svg width="8" height="8" viewBox="0 0 10 10"><circle cx="5" cy="5" r="3.8" fill="none" stroke="#ffffff" stroke-width="1"/><path d="M1.2 5 H8.8 M5 1.2 Q2.8 5 5 8.8 M5 1.2 Q7.2 5 5 8.8" stroke="#ffffff" stroke-width="0.8" fill="none"/></svg>
          </span>
          www.korvaneplumbing.example
        </li>
      </ul>

      <p class="credentials-text">ABN- 42 198 603 771, LIC- 516042D</p>
      <div class="tool-art" role="img" aria-label="Two crossed pipe wrenches illustration"></div>
    </section>
  </main>
</body>
</html>
```